Financial Service Company Need Business Card Design

This is a new startup company, first of its kind to offer this service. We facilitate the movement of deposit funds electronically between home buyers and real estate brokerages.Our customers are REALTORS®, real estate brokerages, and home buyers, we identify ourselves as a financial/technology company.
Not looking for anything too flashy. Just a clean design that shows the logo, contact info, etc. Company colors can be seen on attached logo, and 'coming soon page'
www.plumvault.ca
Industry/Entity Type
Business
Contact Information for Business Card

```html
<!DOCTYPE html>
<html lang="en">
<head>
<meta charset="utf-8">
<title>PlumVault Business Cards</title>
<link rel="stylesheet" href="https://fonts.googleapis.com/css2?family=Ubuntu:wght@400;500&display=swap">
<style>
  :root {
    --bg: #ece6dd;
    --card: #ffffff;
    --orange: #de4a1f;
    --blush: #dcb2aa;
    --ink: #555759;
    --ink-soft: #6b6d70;
    --shadow: rgba(60, 45, 30, 0.18);
  }
  * { box-sizing: border-box; margin: 0; padding: 0; }
  html, body { width: 1200px; height: 1000px; overflow: hidden; }
  body {
    background: var(--bg);
    font-family: "Ubuntu", "Segoe UI", sans-serif;
    position: relative;
  }
  .card {
    position: absolute;
    width: 490px;
    height: 280px;
    background: var(--card);
    border-radius: 6px;
    box-shadow: 0 10px 28px var(--shadow);
    overflow: hidden;
  }
  .brand {
    display: flex;
    align-items: center;
    gap: 10px;
    color: var(--ink);
    font-weight: 500;
    letter-spacing: -0.5px;
    white-space: nowrap;
  }
  .brand-square {
    background: var(--orange);
    flex: none;
  }

  /* Front */
  .card-front { left: 70px; top: 300px; }
  .front-band {
    position: absolute;
    left: 14px; right: 14px;
    height: 52px;
    background: var(--orange);
    border-radius: 8px;
  }
  .front-band.top { top: 14px; }
  .front-band.bottom { bottom: 14px; }
  .front-frame {
    position: absolute;
    left: 14px; right: 14px;
    top: 80px; bottom: 80px;
    border: 1.5px solid var(--orange);
    border-radius: 14px;
    display: flex;
    align-items: center;
    justify-content: center;
  }
  .card-front .brand { font-size: 34px; }
  .card-front .brand-square { width: 26px; height: 26px; }

  /* Back */
  .card-back { left: 640px; top: 300px; }
  .back-stripes { position: absolute; right: 0; top: 0; }
  .card-back .brand {
    position: absolute;
    left: 30px; top: 118px;
    font-size: 24px;
  }
  .card-back .brand-square { width: 18px; height: 18px; }
  .contact-list {
    position: absolute;
    left: 30px; top: 162px;
    list-style: none;
    font-size: 13px;
    color: var(--ink-soft);
  }
  .contact-list li {
    display: flex;
    align-items: center;
    gap: 10px;
    height: 22px;
    white-space: nowrap;
  }
  .contact-list svg { width: 12px; height: 12px; fill: var(--ink); flex: none; }

  /* Standalone lockup */
  .brand-lockup {
    position: absolute;
    left: 776px; top: 812px;
    font-size: 44px;
  }
  .brand-lockup .brand-square { width: 40px; height: 40px; }
</style>
</head>
<body>

  <section class="card card-front" aria-label="Business card front">
    <div class="front-band top"></div>
    <div class="front-frame">
      <div class="brand"><span class="brand-square"></span>PlumVault</div>
    </div>
    <div class="front-band bottom"></div>
  </section>

  <section class="card card-back" aria-label="Business card back">
    <svg class="back-stripes" width="300" height="150" viewBox="0 0 300 150" aria-hidden="true">
      <polygon points="30,0 120,0 70,110 0,110 0,66" fill="var(--blush)"/>
      <polygon points="150,0 240,0 190,110 100,110" fill="var(--blush)"/>
      <polygon points="270,0 300,0 300,110 220,110" fill="var(--blush)"/>
    </svg>
    <div class="brand"><span class="brand-square"></span>PlumVault</div>
    <ul class="contact-list">
      <li><svg viewBox="0 0 12 12"><path d="M3 1l2 2-1 1.5c.6 1.4 1.6 2.4 3 3L8.5 6.5l2 2-1.5 2C5 10 2 7 1.5 2.5z"/></svg>+ 1 416 - 555 - 0142</li>
      <li><svg viewBox="0 0 12 12"><path d="M1 2.5h10v7H1zM1.6 3l4.4 3.5L10.4 3v1L6 7.5 1.6 4z"/></svg>hello@plumvault.ca</li>
      <li><svg viewBox="0 0 12 12"><circle cx="6" cy="6" r="5"/></svg>www.plumvault.ca</li>
      <li><svg viewBox="0 0 12 12"><path d="M6 1a3.5 3.5 0 0 1 3.5 3.5C9.5 7 6 11 6 11S2.5 7 2.5 4.5A3.5 3.5 0 0 1 6 1z"/></svg>120 Harbour Lane, Toronto 54321</li>
    </ul>
  </section>

  <div class="brand brand-lockup"><span class="brand-square"></span>PlumVault</div>

</body>
</html>
```